Business Card Design for Telecommunications and IT Solutions company "ORIV"

BC for telecommunications company name "ORIV" with slogan "Telecom & IT Solutions"

should have the full name as above "ORIV" and the slogan
color reqiured black, red (dark) and white

simple, professional, serious, modern design is required

1 side of business card have a full details, contacts and logo
other side have only the logo, website and full company name "ELORIV Company for Telecommunications service & Information Technology LLC"

i have attached the logo and current business card sample and note that the logo was changed not the same in the attached business card

Industry/Entity Type

Telecommunications

Contact Information for Business Card

Full name: Tamir Hudin Al Qarsi
Job title: General Manager
Mobile no: +964xxxxxxxxx
email: tamir@oriv-example.net
full name of the company: ELORIV Company Telecommunications Services & Information Technology LLC.
website: www.oriv-example.net
address: Tulip Dist. 347/6 HarunQadi, Basra, Iraq

Requirements
Must have
• two languages in the same side of business card (English, Arabic) for only the name and title

```html
<!DOCTYPE html>
<html lang="en">
<head>
<meta charset="utf-8">
<title>ORIV Business Card</title>
<link href="https://fonts.googleapis.com/css2?family=Open+Sans:wght@400;600;700&family=Noto+Serif:wght@400&family=Noto+Sans+Arabic:wght@400;600&display=swap" rel="stylesheet">
<style>
  :root {
    --bg: #e4e2e0;
    --card: #ffffff;
    --ink: #161616;
    --red: #b3121b;
    --band: #c8c8ca;
    --shadow: rgba(0,0,0,0.14);
  }
  * { box-sizing: border-box; margin: 0; padding: 0; }
  html, body { width: 1200px; height: 1189px; overflow: hidden; }
  body { background: var(--bg); font-family: "Open Sans", Arial, sans-serif; color: var(--ink); position: relative; }

  .card { position: absolute; left: 170px; width: 860px; height: 490px; background: var(--card); box-shadow: 0 10px 28px var(--shadow); overflow: hidden; }
  .card--front { top: 70px; }
  .card--back { top: 630px; }

  .brand { position: absolute; display: flex; flex-direction: column; align-items: center; }
  .brand__mark { display: flex; align-items: center; gap: 16px; }
  .brand__dot { width: 26px; height: 26px; border-radius: 50%; background: var(--red); }
  .brand__name { font-weight: 700; font-size: 86px; line-height: 1; color: var(--red); letter-spacing: 2px; }
  .brand__slogan { font-family: "Noto Serif", Georgia, serif; font-size: 19px; margin-top: 10px; color: var(--ink); }

  .card--front .brand { left: 0; right: 0; top: 90px; }
  .company { position: absolute; left: 0; right: 0; top: 262px; text-align: center; }
  .company__short { font-weight: 700; font-size: 26px; }
  .company__full { font-size: 21px; margin-top: 4px; }
  .band { position: absolute; left: 0; right: 0; background: var(--band); display: flex; align-items: center; }
  .card--front .band { top: 355px; height: 80px; justify-content: center; }
  .arabic { font-family: "Noto Sans Arabic", Tahoma, sans-serif; direction: rtl; }
  .company__arabic { font-size: 24px; font-weight: 600; }

  .card--back .brand { left: 40px; width: 330px; top: 150px; }
  .divider { position: absolute; left: 400px; top: 40px; width: 1px; height: 330px; background: var(--red); }
  .person { position: absolute; left: 440px; top: 52px; }
  .person__name { font-size: 30px; font-weight: 600; line-height: 1.1; }
  .person__title { font-size: 20px; font-weight: 600; }
  .person__name-ar { font-size: 24px; font-weight: 600; text-align: left; margin-top: 8px; direction: rtl; display: inline-block; }
  .person__title-ar { font-size: 13px; display: block; margin-top: -2px; }
  .contacts { position: absolute; left: 440px; top: 250px; list-style: none; }
  .contacts li { display: flex; align-items: center; gap: 14px; font-size: 21px; line-height: 32px; }
  .icon { width: 22px; height: 22px; background: var(--red); display: flex; align-items: center; justify-content: center; }
  .card--back .band { top: 395px; height: 70px; justify-content: flex-end; padding-right: 60px; }
  .address { font-size: 26px; font-weight: 600; }
</style>
</head>
<body>
  <section class="card card--front">
    <div class="brand">
      <div class="brand__mark"><span class="brand__dot"></span><span class="brand__name">ORIV</span></div>
      <div class="brand__slogan">Telecom &amp; IT Solutions</div>
    </div>
    <div class="company">
      <p class="company__short">ELORIV Company</p>
      <p class="company__full">Telecommunications Services &amp; Information Technology LLC.</p>
    </div>
    <div class="band">
      <p class="arabic company__arabic">شركة إلوريف لخدمات الاتصالات و تقنية المعلومات المحدودة</p>
    </div>
  </section>

  <section class="card card--back">
    <div class="brand">
      <div class="brand__mark"><span class="brand__dot"></span><span class="brand__name">ORIV</span></div>
      <div class="brand__slogan">Telecom &amp; IT Solutions</div>
    </div>
    <div class="divider"></div>
    <div class="person">
      <p class="person__name">Tamir Hudin Al Qarsi</p>
      <p class="person__title">General Manager</p>
      <p class="arabic person__name-ar">تامر هودين القرصي<span class="person__title-ar">المدير المفوض</span></p>
    </div>
    <ul class="contacts">
      <li><span class="icon"><svg width="14" height="14" viewBox="0 0 24 24"><path fill="#fff" d="M6.6 10.8a15 15 0 0 0 6.6 6.6l2.2-2.2c.3-.3.7-.4 1-.2 1.1.4 2.3.6 3.6.6.6 0 1 .4 1 1V20c0 .6-.4 1-1 1A17 17 0 0 1 3 4c0-.6.4-1 1-1h3.5c.6 0 1 .4 1 1 0 1.3.2 2.5.6 3.6.1.3 0 .7-.2 1z"/></svg></span>+964xxxxxxxxx</li>
      <li><span class="icon"><svg width="14" height="14" viewBox="0 0 24 24"><rect x="2" y="5" width="20" height="14" fill="none" stroke="#fff" stroke-width="2"/><path d="M2 6l10 7 10-7" fill="none" stroke="#fff" stroke-width="2"/></svg></span>tamir@oriv-example.net</li>
      <li><span class="icon"><svg width="14" height="14" viewBox="0 0 24 24"><circle cx="12" cy="12" r="9" fill="none" stroke="#fff" stroke-width="2"/><path d="M3 12h18M12 3c3 3 3 15 0 18M12 3c-3 3-3 15 0 18" fill="none" stroke="#fff" stroke-width="1.6"/></svg></span>www.oriv-example.net</li>
    </ul>
    <div class="band">
      <p class="address">Tulip Dist. 347/6 HarunQadi, Basra, Iraq</p>
    </div>
  </section>
</body>
</html>
```